Real Estate Website - Phase I

We are looking to re-design our company website completely.
This will be for a real estate company which focuses on multiple lines of business/customers, including

1) Buyers - Investors, Owner Occupants
2) Sellers - Short Sales, Limited Services/Flat Fee, and Corporate/REO clients (the last being our core current customer)
3) Other Services: Default Services, Institutional Property Management, Field and Inspection Services
4) Agent FAQ's, instructions, etc to tie into our web-based offer management systems

For a brief understanding of what we do - Please see www.plavetrix.com. Current site does not address all of our current services.

Website must be able to be edited/added onto over time. We are also looking at redirects so that certain pages/sections can be given unique domain names to drive core customers to.

We work both with normal agents and buyers and large scale financial institutions, therefore our focus must be specific to each unique group based on the applicable page(s).

We had an incorrect amount in this brief.  It has since been corrected.

Please re-review.

Industry/Entity Type

Real Estate

Requirements
Must have
• *Property Search/Display - By various criteria AND by map
*Property Management back end for putting in new properties
*MObile Version or Mobile Friendly
*Analytics
*Contact Management and Lead Capture functions, including ability to export or use from site for email marketing campaigns. Lead capture must be able to sort by various criteria to tailor campaigns, ability to send out auto notices to staff and those signing up, etc.
* Signup option w/ functions for viewing not yet on market properties (subscription). This needs to be able to let buyers set search criteria and be auto notified whenever a property was listed or adjusted that met their criteria.
* SEO Optimization
* Syndication options to allow ease of syndication
* FAQ's and assistance pages to agents working with us
* Blog, social media boxes
* Ability for buyers to submit initial offers direct
* Functions and pages specific to below, with ability to cross promote and track (inquiry forms, etc to the below)
*Dedicated or preferred lender(s)
* Preferred vendors, etc

```html
<!DOCTYPE html>
<html lang="en">
<head>
<meta charset="utf-8">
<title>Harbor Line REO</title>
<link href="https://fonts.googleapis.com/css2?family=Open+Sans:ital,wght@0,400;0,600;0,700;1,400&display=swap" rel="stylesheet">
<style>
:root{
  --blue:#3d3db0;
  --blue-dark:#2e2e96;
  --blue-light:#5656c8;
  --ink:#2a2a6a;
  --text:#444;
  --muted:#8a8a8a;
  --panel:#efefef;
  --panel-line:#d4d4d4;
  --lavender:#e6e6fb;
  --price:#d23a12;
}
*{box-sizing:border-box;margin:0;padding:0}
html,body{width:1200px;height:1200px;overflow:hidden;background:#fff;font-family:"Open Sans",sans-serif;color:var(--text)}
.abs{position:absolute}
.band{background:linear-gradient(var(--blue-light),var(--blue-dark))}
.brand{left:316px;top:26px;display:flex;align-items:center;gap:6px}
.brand-mark{width:31px;height:33px;background:var(--blue-dark)}
.brand-name{font-size:16px;font-weight:600;color:var(--ink);line-height:1.1;width:110px}
.tagline{left:314px;top:65px;font-size:7px;color:#555}
.userlinks{right:316px;top:21px;font-size:7px;color:var(--blue)}
.btn{background:linear-gradient(var(--blue-light),var(--blue-dark));color:#fff;display:flex;align-items:center;justify-content:center;font-size:7.5px}
.nav{left:242px;top:80px;width:716px;height:24px}
.nav ul{list-style:none;display:flex;margin-left:74px;height:100%}
.nav li{color:#fff;font-size:7.5px;padding:0 7px;display:flex;align-items:center}
.nav li.active{background:var(--blue-light)}
.hero{left:306px;top:108px;width:587px;height:253px;background:var(--panel)}
.photo{border:2px solid #ccc}
.thumb-arrow{width:16px;height:16px;border:1px solid #aaa;border-radius:50%;background:#fff}
.search{left:734px;top:112px;width:154px;height:243px;border:1px solid var(--panel-line);background:#f6f6f6}
.panel-head{color:#fff;display:flex;align-items:center;padding-left:12px}
.search .panel-head{height:26px;justify-content:center;font-size:10px;font-weight:600;padding:0}
.select{height:18px;border:1px solid #ccc;background:#fff;font-size:7px;color:#666;padding-left:6px;display:flex;align-items:center}
.select::after{content:"";position:absolute;right:0;top:0;width:18px;height:16px;background:var(--blue)}
.select svg{position:absolute;right:5px;top:6px;z-index:1}
.tabs{left:314px;top:384px;display:flex;gap:9px;font-size:10px;color:var(--blue)}
.tabs span{padding:1px 6px}
.tabs .on{background:var(--blue);color:#fff}
.rule{height:1px;background:var(--blue)}
.intro{left:314px;top:416px;width:410px;font-size:7.4px;line-height:12px;color:#444}
.listings{left:313px;top:497px;width:411px;height:511px;border:1px solid #ccc;background:#f2f2f2}
.listings>.panel-head{height:26px;font-size:10.5px;letter-spacing:.5px}
.item{position:absolute;left:12px;width:372px;height:143px}
.item .pic{left:0;top:0;width:178px;height:102px;border:2px solid #ccc}
.item h3{position:absolute;left:187px;top:3px;font-size:11px;color:#555;font-weight:700;letter-spacing:.4px}
.item .city{left:189px;top:20px;font-size:7px;color:#555;font-weight:600}
.item .price{left:188px;top:31px;font-size:11px;color:var(--price);font-weight:700}
.facts{left:189px;width:182px;height:25px;background:#e9e9e9;font-size:7px;color:#888;padding:4px 0 0 8px;line-height:12px}
.facts i{display:inline-block;width:6px;height:6px;border:1px solid #999;margin-right:5px}
.item .status{left:3px;top:121px;font-size:7px;color:#999;font-style:italic}
.item .status b{color:var(--blue);font-weight:400}
.item .view{left:288px;top:115px;width:81px;height:17px;font-weight:700;letter-spacing:.5px}
.item .divide{left:0;top:142px;width:372px;height:1px;border-top:1px dotted #999}
.side{border:1px solid var(--panel-line);background:#f6f6f6}
.side .panel-head{height:23px;font-size:7.5px}
.map{left:734px;top:698px;width:153px;height:275px;border:2px solid #ccc;background:linear-gradient(135deg,#f3eed8,#f2e1a8 50%,#e8e4d4)}
.footer{left:242px;top:1028px;width:716px;height:139px;background:var(--lavender)}
.bottom{left:242px;top:1167px;width:716px;height:31px;color:#fff}
.ftext{font-family:Arial,sans-serif}
</style>
</head>
<body>

<header>
  <div class="abs brand"><span class="brand-mark"></span><span class="brand-name">Harbor Line REO</span></div>
  <div class="abs tagline">Cyprus property For Sale and For Rent</div>
  <div class="abs userlinks">Welcome , Guest &nbsp;|&nbsp; Sing In &nbsp;|&nbsp; sing Up</div>
  <div class="abs btn" style="left:802px;top:44px;width:82px;height:18px">Submit Property &nbsp;&gt;&gt;</div>
  <nav class="abs nav band">
    <ul><li>HOME</li><li>BLOG</li><li class="active">FEATURE</li><li>FEATURED</li><li>HOME BUYERS</li><li>HOME SELLERS</li><li>PROPERTIES</li><li>UNCATEGORIZED</li></ul>
  </nav>
</header>

<section class="abs hero">
  <div class="abs photo" role="img" aria-label="Featured two-storey family house with trees" style="left:8px;top:4px;width:408px;height:181px;background:linear-gradient(#4c7a3a,#9aa08e 55%,#8c8a80)"></div>
  <div class="abs photo" role="img" aria-label="Thumbnail: suburban houses" style="left:8px;top:197px;width:67px;height:49px;background:linear-gradient(#a9c4e4,#9a9a8a)"></div>
  <div class="abs photo" role="img" aria-label="Thumbnail: yellow house" style="left:85px;top:197px;width:67px;height:49px;background:linear-gradient(#7fa6d6,#c9a24a)"></div>
  <div class="abs photo" role="img" aria-label="Thumbnail: apartment building with pool" style="left:164px;top:197px;width:67px;height:49px;background:linear-gradient(#6f9fd8,#d8d0c0)"></div>
  <div class="abs photo" role="img" aria-label="Thumbnail: villa with red roof" style="left:243px;top:197px;width:67px;height:49px;background:linear-gradient(#8fb8e6,#c0603a)"></div>
  <div class="abs photo" role="img" aria-label="Thumbnail: house lit at night" style="left:323px;top:197px;width:67px;height:49px;background:linear-gradient(#1d2a60,#7a5a3a)"></div>
  <div class="abs thumb-arrow" style="left:397px;top:201px"><svg width="14" height="14"><path d="M6 4l3 3-3 3" stroke="#888" fill="none"/></svg></div>
  <div class="abs thumb-arrow" style="left:397px;top:228px"><svg width="14" height="14"><path d="M8 4l-3 3 3 3" stroke="#888" fill="none"/></svg></div>
</section>

<aside class="abs search">
  <div class="panel-head band">QUICK SEARCH</div>
  <div class="abs" style="left:10px;top:40px;font-size:8px;color:var(--blue)">For sale</div>
  <div class="abs" style="right:10px;top:40px;font-size:8px;color:var(--blue)">For Rent</div>
  <div class="abs select" style="left:10px;top:64px;width:133px">Location<svg width="8" height="5"><path d="M0 0h8L4 5z" fill="#fff"/></svg></div>
  <div class="abs select" style="left:10px;top:91px;width:133px">Property type<svg width="8" height="5"><path d="M0 0h8L4 5z" fill="#fff"/></svg></div>
  <div class="abs select" style="left:10px;top:117px;width:133px">Square Feet<svg width="8" height="5"><path d="M0 0h8L4 5z" fill="#fff"/></svg></div>
  <div class="abs select" style="left:10px;top:144px;width:63px">Beds<svg width="8" height="5"><path d="M0 0h8L4 5z" fill="#fff"/></svg></div>
  <div class="abs select" style="left:80px;top:144px;width:63px">Baths<svg width="8" height="5"><path d="M0 0h8L4 5z" fill="#fff"/></svg></div>
  <div class="abs select" style="left:10px;top:170px;width:63px">Min price<svg width="8" height="5"><path d="M0 0h8L4 5z" fill="#fff"/></svg></div>
  <div class="abs select" style="left:80px;top:170px;width:63px">Max price<svg width="8" height="5"><path d="M0 0h8L4 5z" fill="#fff"/></svg></div>
  <div class="abs btn" style="left:79px;top:199px;width:64px;height:17px">Search</div>
  <div class="abs" style="right:6px;top:225px;font-size:8px;color:var(--blue)">Advanced Search</div>
</aside>

<section>
  <div class="abs tabs"><span class="on">Buyers</span><span style="padding:1px 0">Sellers</span><span>Other Services</span></div>
  <div class="abs rule" style="left:314px;top:402px;width:410px"></div>
  <div class="abs intro">
    <p style="margin-bottom:6px">If you are interested in purchasing an available property or obtaining further information, click on For Buyers.</p>
    <p>You can also access up-to-date information and request a showing on all of our area listings at the touch of a button by visiting our Current Listings page.</p>
    <p style="margin-top:6px;font-size:6.5px;color:var(--blue)">Read more &gt;&gt;</p>
  </div>
</section>

<section class="abs listings">
  <div class="panel-head band">LATEST LISTINGS</div>

  <article class="item" style="top:37px">
    <div class="abs pic" role="img" aria-label="Two-storey villa with red tile roof" style="background:linear-gradient(#9cc2ea,#e9e3d8 50%,#6a9a4a)"></div>
    <h3>1147 Alder Crest Court</h3>
    <div class="abs city">Lakeview,CA 90210</div>
    <div class="abs price">$192,000</div>
    <div class="abs facts" style="top:51px"><i></i>2198 sqft &nbsp;&nbsp;&nbsp;<i></i>2 bedrooms<br><i></i>4 baths</div>
    <div class="abs facts" style="top:82px"><i></i>2 Car Garage<br><i></i>Listed 3 day 45 min ago</div>
    <div class="abs status">Property Status: <b>For Rent</b></div>
    <div class="abs btn view">VIEW LISTING</div>
    <div class="abs divide"></div>
  </article>

  <article class="item" style="top:196px">
    <div class="abs pic" role="img" aria-label="Red brick family house with lawn" style="background:linear-gradient(#b8d4ee,#8a4030 45%,#4e8a3a)"></div>
    <h3>1147 Alder Crest Court</h3>
    <div class="abs city">Lakeview,CA 90210</div>
    <div class="abs price">$192,000</div>
    <div class="abs facts" style="top:51px"><i></i>2198 sqft &nbsp;&nbsp;&nbsp;<i></i>2 bedrooms<br><i></i>4 baths</div>
    <div class="abs facts" style="top:82px"><i></i>2 Car Garage<br><i></i>Listed 3 day 45 min ago</div>
    <div class="abs status">Property Status: <b>For Rent</b></div>
    <div class="abs btn view">VIEW LISTING</div>
    <div class="abs divide"></div>
  </article>

  <article class="item" style="top:355px">
    <div class="abs pic" role="img" aria-label="Brick house lit up at dusk" style="background:linear-gradient(#1a2a70,#3a3a5a 45%,#a07040 80%,#2a3a20)"></div>
    <h3>1147 Alder Crest Court</h3>
    <div class="abs city">Lakeview,CA 90210</div>
    <div class="abs price">$192,000</div>
    <div class="abs facts" style="top:51px"><i></i>2198 sqft &nbsp;&nbsp;&nbsp;<i></i>2 bedrooms<br><i></i>4 baths</div>
    <div class="abs facts" style="top:82px"><i></i>2 Car Garage<br><i></i>Listed 3 day 45 min ago</div>
    <div class="abs status">Property Status: <b>For Rent</b></div>
    <div class="abs btn view">VIEW LISTING</div>
  </article>
</section>

<aside>
  <div class="abs side" style="left:734px;top:386px;width:153px;height:122px">
    <div class="panel-head band">SUBSCRIBE TO NEWSLETTER!</div>
    <div class="abs" style="left:12px;top:32px;font-size:7px;color:#444">Stay updated with all latest news.</div>
    <div class="abs" style="left:14px;top:54px;width:127px;height:20px;border:1px solid #ccc;background:#fff;font-size:7px;padding:5px;color:#333">Email</div>
    <div class="abs btn" style="left:15px;top:84px;width:79px;height:23px">Subscribe now!</div>
  </div>

  <div class="abs side" style="left:734px;top:530px;width:153px;height:147px">
    <div class="panel-head band">Follow us on Friendlink</div>
    <div class="abs" role="img" aria-label="Page avatar" style="left:9px;top:30px;width:28px;height:27px;background:linear-gradient(#b6a08a,#5a5070)"></div>
    <div class="abs" style="left:46px;top:29px;font-size:7px;color:#333">Kestrelo.com</div>
    <div class="abs" style="left:48px;top:43px;width:25px;height:11px;border:1px solid #bbc;background:#eef;font-size:6px;color:var(--blue);padding-left:5px">Like</div>
    <div class="abs" style="left:11px;top:61px;font-size:7px;color:#333">105 people like Kestrelo.com</div>
    <svg class="abs" style="left:9px;top:73px" width="130" height="59">
      <g fill="#000"><rect x="0" y="0" width="30" height="27"/><rect x="33" y="0" width="30" height="27"/><rect x="65" y="0" width="30" height="27"/><rect x="98" y="0" width="30" height="27"/><rect x="0" y="31" width="30" height="27"/><rect x="33" y="31" width="30" height="27"/><rect x="65" y="31" width="30" height="27"/><rect x="98" y="31" width="30" height="27"/></g>
    </svg>
  </div>

  <div class="abs map" role="img" aria-label="Street map with property location markers"></div>
</aside>

<footer>
  <div class="abs footer ftext">
    <div class="abs" style="left:72px;top:9px;font-size:8px;color:var(--blue)">Call: (555) 014-2290</div>
    <div class="abs rule" style="left:72px;top:26px;width:409px;background:#7777bb"></div>
    <div class="abs" style="left:79px;top:42px;font-size:7px;color:#333">Sell with Marin</div>
    <div class="abs" style="left:72px;top:56px;font-size:7px;color:#333">Featured on Dwellbook</div>
    <div class="abs" role="img" aria-label="Interior room photo" style="left:72px;top:70px;width:69px;height:47px;background:linear-gradient(#c89a6a,#7a5a3a)"></div>
    <div class="abs btn" style="left:116px;top:123px;width:11px;height:11px;padding:0"><svg width="6" height="7"><path d="M5 0L1 3.5 5 7" stroke="#fff" fill="none"/></svg></div>
    <div class="abs btn" style="left:130px;top:123px;width:11px;height:11px;padding:0"><svg width="6" height="7"><path d="M1 0l4 3.5L1 7" stroke="#fff" fill="none"/></svg></div>
    <div class="abs" style="left:192px;top:41px;font-size:8px;font-weight:700;color:#444">Testimonials</div>
    <div class="abs" style="left:192px;top:60px;width:130px;font-size:7px;line-height:8.5px;color:#777">Lorem ipsum dolor sit amet, con-sectetur adipisicing elit, sed do eius-mod tempor incididunt ut labore et dolore magna aliqua.</div>
    <div class="abs" style="left:192px;top:101px;font-size:8px;font-weight:700;color:#555">-Oren.</div>
    <div class="abs" style="left:353px;top:41px;font-size:8px;font-weight:700;color:#444">Connect With Name</div>
    <div class="abs" style="left:354px;top:59px;width:18px;height:18px;border-radius:50%;background:var(--blue-dark)"></div>
    <div class="abs" style="left:380px;top:63px;font-size:8px;font-weight:700;color:#444">Friendlink</div>
    <div class="abs" style="left:354px;top:86px;width:18px;height:18px;border-radius:50%;background:#5aa8d8"></div>
    <div class="abs" style="left:380px;top:90px;font-size:8px;font-weight:700;color:#444">Chirpline</div>
    <div class="abs side" style="left:491px;top:8px;width:153px;height:122px">
      <div class="panel-head band">LATEST UPDATES</div>
      <div class="abs" style="left:11px;top:36px;width:130px;font-size:7px;line-height:8.5px;color:#777">Lorem ipsum dolor sit amet, con-sectetur adipisicing elit, sed do eius-mod tempor.</div>
      <div class="abs" style="left:11px;top:75px;width:130px;font-size:7px;line-height:8.5px;color:#777">Lorem ipsum dolor sit amet, con-sectetur adipisicing elit, sed do eius-mod tempor.</div>
    </div>
  </div>
  <div class="abs bottom band ftext">
    <div class="abs" style="left:72px;top:10px;font-size:7px">Site Mape &nbsp;&nbsp;&nbsp;|&nbsp;&nbsp;&nbsp; Search Tearch &nbsp;&nbsp;&nbsp;|&nbsp;&nbsp;&nbsp; Terms Orders and Retuns &nbsp;&nbsp;&nbsp;|&nbsp;&nbsp;&nbsp; Contactr Us</div>
    <div class="abs" style="right:70px;top:14px;font-size:5.5px">Copyright © 2012 Brightmere. All rights reserved.</div>
  </div>
</footer>

</body>
</html>
```